Business Card for Business consulting practice

Need a design for a consultant business card. Simple and elegant.
I need the following information on the card:
Logo: (see uploaded file)
Company name: Calmora Advisory Group
Name: Dana Weltrup
Title: Managing Director - Aerospace and Defence
Phone #: 514-268-3917
e-mail: dana.weltrup@calmora-example.com
Website: www.calmora-example.com
Tagline: Proposals Management and Capture support for complex procurements

```html
<!DOCTYPE html>
<html lang="en">
<head>
<meta charset="utf-8">
<title>Calmora Advisory Group — Business Card</title>
<link rel="stylesheet" href="https://fonts.googleapis.com/css2?family=Cinzel:wght@500&family=Oswald:wght@600&family=Arimo:wght@400&display=swap">
<style>
  :root {
    --backdrop: #2b2d30;
    --card-navy: #0b2d42;
    --card-navy-soft: #10364d;
    --accent-cyan: #1c90c2;
    --text-white: #ffffff;
    --emboss-line: #1a4560;
  }
  * { box-sizing: border-box; margin: 0; padding: 0; }
  html, body {
    width: 1200px; height: 1015px; overflow: hidden;
    background: var(--backdrop);
  }
  .sheet {
    width: 1200px; height: 1015px;
    display: flex; flex-direction: column; align-items: center; justify-content: center;
    gap: 48px;
  }
  .card {
    position: relative;
    width: 760px; height: 434px;
    background: var(--card-navy);
    box-shadow: 0 10px 30px rgba(0,0,0,.45);
    overflow: hidden;
  }

  /* Front */
  .brand {
    position: absolute; left: 0; right: 0; top: 112px;
    text-align: center;
    font-family: "Cinzel", serif; font-weight: 500;
    color: var(--text-white);
  }
  .brand-name { font-size: 62px; letter-spacing: 3px; line-height: 1; }
  .brand-sub {
    display: flex; align-items: center; justify-content: center; gap: 14px;
    margin-top: 10px;
    font-size: 16px; letter-spacing: 7px; color: var(--text-white);
  }
  .brand-sub::before, .brand-sub::after {
    content: ""; width: 90px; height: 1px; background: var(--accent-cyan);
  }
  .tagline-rule {
    position: absolute; left: 40px; right: 40px; bottom: 78px;
    height: 1px; background: var(--accent-cyan);
  }
  .tagline {
    position: absolute; left: 40px; right: 40px; bottom: 40px;
    text-align: center; white-space: nowrap;
    font-family: "Oswald", sans-serif; font-weight: 600;
    font-size: 20px; line-height: 26px; letter-spacing: 0;
    text-transform: uppercase;
    color: var(--text-white);
  }

  /* Back */
  .holder {
    position: absolute; left: 60px; top: 120px;
    font-family: "Arimo", sans-serif; color: var(--text-white);
  }
  .holder-name {
    font-family: "Cinzel", serif; font-weight: 500;
    font-size: 34px; letter-spacing: 1.5px; color: var(--accent-cyan);
    line-height: 1.1;
  }
  .holder-role { font-size: 19px; line-height: 1.3; margin-top: 4px; padding-left: 16px; }
  .contact-list {
    position: absolute; left: 80px; bottom: 62px;
    list-style: none;
    font-family: "Arimo", sans-serif; font-size: 19px; color: var(--text-white);
  }
  .contact-list li { display: flex; align-items: center; gap: 10px; line-height: 1.45; }
  .contact-list svg { width: 19px; height: 19px; flex: none; }
  .emboss-mark {
    position: absolute; right: 50px; top: 50px;
    width: 270px; height: 270px;
  }
</style>
</head>
<body>
<main class="sheet">

  <section class="card card-front" aria-label="Card front">
    <div class="brand">
      <div class="brand-name">Calmora</div>
      <div class="brand-sub">Advisory Group</div>
    </div>
    <div class="tagline-rule"></div>
    <p class="tagline">Proposals Management and Capture Support for Complex Procurements</p>
  </section>

  <section class="card card-back" aria-label="Card back">
    <svg class="emboss-mark" viewBox="0 0 270 270" aria-hidden="true">
      <circle cx="135" cy="135" r="125" fill="var(--card-navy-soft)" stroke="var(--emboss-line)" stroke-width="2"/>
    </svg>
    <div class="holder">
      <h1 class="holder-name">Dana Weltrup</h1>
      <p class="holder-role">Managing Director<br>Aerospace and Defence</p>
    </div>
    <ul class="contact-list">
      <li>
        <svg viewBox="0 0 24 24" aria-hidden="true"><path fill="var(--accent-cyan)" d="M6.6 10.8a15.1 15.1 0 0 0 6.6 6.6l2.2-2.2c.3-.3.7-.4 1-.2 1.1.4 2.3.6 3.600.6.6 0 1 .4 1 1V20c0 .6-.4 1-1 1A17 17 0 0 1 3 4c0-.6.4-1 1-1h3.5c.6 0 1 .4 1 1 0 1.3.2 2.5.6 3.6.1.3 0 .7-.2 1z"/></svg>
        514-268-3917
      </li>
      <li>
        <svg viewBox="0 0 24 24" aria-hidden="true"><path fill="var(--accent-cyan)" d="M2 5h20v14H2z"/><path fill="none" stroke="var(--card-navy)" stroke-width="1.6" d="M2 5l10 8 10-8"/></svg>
        dana.weltrup@calmora-example.com
      </li>
      <li>
        <svg viewBox="0 0 24 24" aria-hidden="true"><g fill="none" stroke="var(--accent-cyan)" stroke-width="1.8"><circle cx="12" cy="12" r="9.5"/><ellipse cx="12" cy="12" rx="4" ry="9.5"/><path d="M2.5 12h19M4 7h16M4 17h16"/></g></svg>
        www.calmora-example.com
      </li>
    </ul>
  </section>

</main>
</body>
</html>
```